We are looking to recreate our Harmon & Company Jobsite Sign. This sign will be placed by the street at each of our jobsites. We want to keep this sign simple, but at the same time, want to add a catching appeal to the design for anyone passing by. We want to stick to a two color scheme (Harmon Blue, and White). Please only use the Company Logo that I have uploaded for this project. Please also see a mock up of what we would like to include on this sign. The Sign Dimensions will be 4' x 8'. Please keep all verbiage uniform with the verbiage on the sample design I have uploaded. LET YOUR CREATIVITY FLOW!

```html
<!DOCTYPE html>
<html lang="en">
<head>
<meta charset="utf-8">
<title>Harmon &amp; Company – 4 × 8 ft Jobsite Sign Options</title>
<link href="https://fonts.googleapis.com/css2?family=Source+Serif+4:wght@600;700&display=swap" rel="stylesheet">
<style>
  :root {
    --harmon-blue: #2e3480;
    --white: #ffffff;
    --board-grey: #b1b1b5;
  }
  * { margin: 0; padding: 0; box-sizing: border-box; }
  html, body {
    width: 900px; height: 1200px; overflow: hidden;
    background: var(--board-grey);
    font-family: "Source Serif 4", Georgia, serif;
  }
  /* 4 ft × 8 ft street sign panel, drawn at 2:1 */
  .sign {
    position: absolute; left: 145px;
    width: 610px; height: 305px; overflow: hidden;
    background: var(--sign-bg);
    color: var(--sign-ink);
    box-shadow: 0 6px 14px rgba(0,0,0,0.25);
  }
  .sign--dark  { top: 199px; --sign-bg: var(--harmon-blue); --sign-ink: var(--white); --band: var(--white); --band-ink: var(--harmon-blue); }
  .sign--light { top: 659px; --sign-bg: var(--white); --sign-ink: var(--harmon-blue); --band: var(--harmon-blue); --band-ink: var(--white); }

  .sign__art { position: absolute; inset: 0; }
  .sign__frame { fill: none; stroke: var(--sign-ink); stroke-width: 1; }
  .sign__swoosh { fill: var(--band); }
  .sign__band { fill: var(--band); stroke: var(--sign-bg); stroke-width: 6; paint-order: stroke; }

  .wordmark {
    position: absolute; left: 86px; top: 36px; width: 204px;
    text-align: right; font-weight: 700; line-height: 1;
  }
  .wordmark__name { display: block; font-size: 45px; letter-spacing: -0.5px; }
  .wordmark__legal { display: block; font-size: 18px; margin-top: 1px; }
  .lockup-divider {
    position: absolute; left: 303px; top: 41px; width: 2px; height: 63px;
    background: var(--sign-ink);
  }
  .trade {
    position: absolute; left: 312px; top: 40px; width: 200px;
    text-align: center; font-weight: 600; font-size: 32px; line-height: 29px;
  }
  .tagline {
    position: absolute; left: 0; right: 0; top: 112px;
    text-align: center; font-weight: 600; font-size: 28px;
  }
  .tagline sup { font-size: 11px; vertical-align: 12px; }
  .location {
    position: absolute; left: 0; right: 0; top: 159px;
    text-align: center; font-weight: 600; font-size: 14px;
  }
  .social {
    position: absolute; left: 90px; top: 237px; display: flex; gap: 3px;
  }
  .social__dot {
    width: 15px; height: 15px; border-radius: 50%;
    background: var(--band-ink);
  }
  .website {
    position: absolute; left: 89px; top: 258px;
    font-weight: 600; font-size: 19px; color: var(--band-ink);
  }
  .contact {
    position: absolute; right: 81px; top: 255px;
    text-align: right; font-weight: 600; font-size: 11px; line-height: 13px;
    color: var(--band-ink);
  }
</style>
</head>
<body>

<section class="sign sign--dark" aria-label="Jobsite sign 4 by 8 feet, blue version">
  <svg class="sign__art" viewBox="0 0 610 305" aria-hidden="true">
    <rect class="sign__frame" x="16.5" y="15.5" width="577" height="240"/>
    <path class="sign__swoosh" d="M238,207 Q450,186 610,226 L610,252 Q430,196 238,211 Z"/>
    <path class="sign__band" d="M0,251 Q300,168 610,250 L610,310 L0,310 Z"/>
  </svg>
  <div class="wordmark"><span class="wordmark__name">Harmon</span><span class="wordmark__legal">&amp; Company, Inc.</span></div>
  <div class="lockup-divider"></div>
  <div class="trade">General<br>Contractors</div>
  <p class="tagline">“We Build Lasting Trust”<sup>®</sup></p>
  <p class="location">Lakemont, Florida</p>
  <div class="social"><span class="social__dot"></span><span class="social__dot"></span><span class="social__dot"></span></div>
  <p class="website">HarmonCompany.net</p>
  <p class="contact">555-014-2290<br>CGC4471023</p>
</section>

<section class="sign sign--light" aria-label="Jobsite sign 4 by 8 feet, white version">
  <svg class="sign__art" viewBox="0 0 610 305" aria-hidden="true">
    <rect class="sign__frame" x="16.5" y="15.5" width="577" height="240"/>
    <path class="sign__swoosh" d="M238,207 Q450,186 610,226 L610,252 Q430,196 238,211 Z"/>
    <path class="sign__band" d="M0,251 Q300,168 610,250 L610,310 L0,310 Z"/>
  </svg>
  <div class="wordmark"><span class="wordmark__name">Harmon</span><span class="wordmark__legal">&amp; Company, Inc.</span></div>
  <div class="lockup-divider"></div>
  <div class="trade">General<br>Contractors</div>
  <p class="tagline">“We Build Lasting Trust”<sup>®</sup></p>
  <p class="location">Lakemont, Florida</p>
  <div class="social"><span class="social__dot"></span><span class="social__dot"></span><span class="social__dot"></span></div>
  <p class="website">HarmonCompany.net</p>
  <p class="contact">555-014-2290<br>CGC4471023</p>
</section>

</body>
</html>
```